Will you marry me post card

I am just looking for a postcard to send my partner that will ask him to marry me.
I plan on creating about 200 of them and mailing them all at once so that he gets them all on the same day.
They should all be similar or could have a few different options.
I would like it simple, elegant, clean and crisp. No images, just text or icons

My only requirement is the text, "will you marry me?" in all lowercase -- any fonts, can be big, small, varying sizes, repeated, whole card, tiny space, don't care...just amazing design. BUT SIMPLE!

```html
<!DOCTYPE html>
<html lang="en">
<head>
<meta charset="utf-8">
<title>will you marry me? postcard</title>
<link rel="stylesheet" href="https://fonts.googleapis.com/css2?family=Questrial&display=swap">
<style>
  :root {
    --magenta: #bf2379;
    --paper: #ffffff;
    --ink: #555555;
    --edge: #3a3a3a;
    --canvas: #ffffff;
  }
  html, body {
    margin: 0;
    padding: 0;
    width: 877px;
    height: 1200px;
    overflow: hidden;
    background: var(--canvas);
  }
  .sheet {
    position: relative;
    width: 877px;
    height: 1200px;
  }
  .card-front {
    position: absolute;
    left: 0;
    top: 0;
    width: 877px;
    height: 583px;
    display: block;
  }
  .proposal {
    font-family: "Questrial", "Century Gothic", sans-serif;
    font-size: 88px;
    fill: var(--paper);
    text-anchor: middle;
    letter-spacing: -1.5px;
  }
  .card-back {
    position: absolute;
    left: 0;
    top: 615px;
    width: 877px;
    height: 585px;
    display: block;
  }
</style>
</head>
<body>
<main class="sheet">
  <svg class="card-front" viewBox="0 0 877 583" xmlns="http://www.w3.org/2000/svg">
    <rect class="front-field" x="0.5" y="0.5" width="876" height="582" fill="var(--magenta)" stroke="var(--edge)" stroke-width="1"/>
    <text class="proposal" x="438" y="288">will you</text>
    <text class="proposal" x="438" y="370">marry me?</text>
  </svg>

  <svg class="card-back" viewBox="0 0 877 585" xmlns="http://www.w3.org/2000/svg">
    <rect class="back-field" x="0.5" y="0.5" width="876" height="584" fill="var(--paper)" stroke="var(--edge)" stroke-width="1"/>
    <line class="message-divider" x1="435" y1="31" x2="435" y2="518" stroke="var(--ink)" stroke-width="1"/>
    <g class="address-lines" stroke="var(--ink)" stroke-width="1">
      <line x1="465" y1="238" x2="835" y2="238"/>
      <line x1="465" y1="297" x2="835" y2="297"/>
      <line x1="465" y1="356" x2="835" y2="356"/>
      <line x1="465" y1="415" x2="835" y2="415"/>
    </g>
  </svg>
</main>
</body>
</html>
```